Digital Asset Exchange (Trading Platform)

We need a design of Digital Asset Exchange Trading Platform.

Please find attached a mock up of VelmoraTrade design this has to be redesigned based on plinor.co.uk style.

Industry/Entity Type

Digital

```html
<!DOCTYPE html>
<html lang="en">
<head>
<meta charset="utf-8">
<title>VelmoraTrade – Digital Asset Exchange</title>
<link href="https://fonts.googleapis.com/css2?family=Cabin:wght@400;500;600;700&display=swap" rel="stylesheet">
<style>
:root{
  --header:#2a2a2a;
  --blue:#0b9bd7;
  --orange:#f7931e;
  --row-a:#3c3c3c;
  --row-b:#464646;
  --cell-text:#d4d4d4;
  --green:#7ed321;
  --red:#e1261c;
  --ink:#333;
  --muted:#888;
  --rule:#dcdcdc;
  --footer:#efefef;
  --chart-bg:#000;
}
*{box-sizing:border-box;margin:0;padding:0}
html,body{width:1200px;height:1050px;overflow:hidden;background:#fff}
body{font-family:"Cabin",sans-serif;color:var(--ink)}
.stage{position:relative;width:1000px;height:875px;transform:scale(1.2);transform-origin:0 0}
.abs{position:absolute}

/* header */
.site-header{left:0;top:0;width:1000px;height:107px;background:var(--header)}
.brand{left:43px;top:30px;display:flex;align-items:center;gap:10px}
.brand-dot{width:44px;height:44px;border-radius:50%;background:var(--orange)}
.brand-name{color:#fff;font-size:27px;font-weight:500}
.top-nav{right:44px;top:13px;font-size:11px;color:#fff}
.top-nav span{margin:0 3px;color:#aaa}
.login-form{left:465px;top:44px;display:flex;gap:7px}
.field{height:25px;background:#fff;border-radius:3px;font-size:11px;color:#999;padding:6px 9px;width:180px}
.btn{height:25px;border-radius:3px;font-size:11px;font-weight:600;color:#fff;padding:6px 0;text-align:center;width:55px}
.btn-login{background:#555;margin-left:1px}
.btn-signup{background:var(--blue)}
.forgot{left:465px;top:75px;font-size:9px;color:#ccc}

/* data tables */
.grid-table{position:absolute;font-size:11px;color:var(--cell-text)}
.grid-table .th{display:flex;height:23px;background:var(--blue);color:#fff;font-weight:600;font-size:12px;align-items:center}
.grid-table .tr{display:flex;height:29px;align-items:center;border-top:1px solid #333}
.grid-table .tr:nth-child(odd){background:var(--row-b)}
.grid-table .tr:nth-child(even){background:var(--row-a)}
.grid-table .c{padding-left:15px;height:100%;display:flex;align-items:center;position:relative}
.grid-table .c + .c{border-left:1px solid #2e2e2e}
.up::before,.down::before{content:"";display:inline-block;width:3px;height:8px;margin-right:3px}
.up::before{background:var(--green)}
.down::before{background:var(--red)}
.sort{position:absolute;right:8px;top:50%;transform:translateY(-50%)}

/* order panel */
.order-tabs{left:512px;top:131px;width:210px;display:flex;height:23px;font-size:12px;font-weight:600;color:#fff}
.order-tabs div{flex:1;padding:5px 15px}
.tab-market{background:var(--orange)}
.tab-limit{background:var(--blue)}
.quote{left:512px;top:154px;width:210px;height:87px;background:#3c3c3c;color:var(--cell-text);font-size:11px}
.quote-row{display:flex;height:58px;border-bottom:1px solid #2e2e2e}
.quote-row > div{flex:1;padding:9px 15px}
.quote-row > div + div{border-left:1px solid #2e2e2e}
.quote-price{font-size:10px;margin-top:3px}
.quote-price b{font-size:17px;color:#fff}
.qty-row{display:flex;height:28px}
.qty-row > div{flex:1;padding:7px 15px}
.qty-row > div + div{border-left:1px solid #2e2e2e}
.input-label{font-size:11px;color:var(--ink)}
.mini-field{height:19px;border:1px solid #bbb;font-size:11px;padding:2px 6px;width:101px;color:var(--ink)}

.book .tr{height:28.75px}
.book .c{width:105px;font-size:11px}
.bid{color:var(--green)}
.ask{color:var(--red)}

/* chart */
.chart-toolbar{left:43px;top:265px;width:445px;height:55px;background:var(--blue)}
.tool{position:absolute;top:15px;height:24px;background:#fff;border-radius:3px;font-size:11px;color:#555;padding:5px 8px}
.tool .caret{position:absolute;right:0;top:0;width:22px;height:24px;background:#555;border-radius:0 3px 3px 0}
.tool .caret::after{content:"";position:absolute;left:8px;top:10px;border:3px solid transparent;border-top-color:#ddd}
.tool .period{position:absolute;right:22px;top:0;width:24px;height:24px;background:#555;color:#fff;padding:5px 5px}
.chart-area{left:43px;top:320px;width:445px;height:320px;background:var(--chart-bg)}

/* history tabs */
.hist-tabs{left:43px;top:663px;width:445px;height:26px;display:flex;border-bottom:2px solid var(--blue);font-size:12px;font-weight:500}
.hist-tabs div{padding:5px 15px;background:#eee;color:#444;margin-right:2px}
.hist-tabs .active{background:var(--blue);color:#fff}

/* sidebar */
.side-title{font-size:16px;font-weight:700;color:var(--blue);padding-bottom:5px;border-bottom:2px solid var(--rule);position:relative}
.side-title::after{content:"";position:absolute;left:0;bottom:-2px;width:110px;height:2px;background:var(--blue)}
.news-item{padding:14px 0 12px;border-bottom:1px solid var(--rule)}
.news-item h3{font-size:12px;font-weight:600;color:#333;white-space:nowrap}
.news-date{font-size:9px;color:var(--muted);margin:3px 0 5px}
.news-item p{font-size:11px;color:#555;line-height:16px}
.post{padding:12px 0 10px;border-bottom:1px solid var(--rule);font-size:11px;color:#555;line-height:17px}
.post a{color:var(--blue);text-decoration:none}
.post-age{font-size:9px;color:var(--muted)}

/* footer */
.site-footer{left:0;top:832px;width:1000px;height:43px;background:var(--footer);font-size:11px;color:#444}
.site-footer .copy{position:absolute;left:43px;top:15px}
.site-footer .links{position:absolute;right:43px;top:15px}
.site-footer span{margin:0 3px;color:#888}
</style>
</head>
<body>
<div class="stage">

  <header class="site-header abs">
    <div class="brand abs"><div class="brand-dot"></div><div class="brand-name">VelmoraTrade</div></div>
    <nav class="top-nav abs">Home <span>|</span> About <span>|</span> Trade <span>|</span> Support</nav>
    <div class="login-form abs">
      <div class="field">Email...</div>
      <div class="field">Password...</div>
      <div class="btn btn-login">LOGIN</div>
      <div class="btn btn-signup">SIGNUP</div>
    </div>
    <div class="forgot abs">Forgot your password?</div>
  </header>

  <!-- market pairs -->
  <div class="grid-table" style="left:43px;top:131px;width:211px">
    <div class="th"><div class="c" style="width:105px">PAIR</div><div class="c" style="border:0">PRICE</div></div>
    <div class="tr"><div class="c" style="width:105px">BTC/USD</div><div class="c down">634.12</div></div>
    <div class="tr"><div class="c" style="width:105px">LTC/USD</div><div class="c down">23.23</div></div>
    <div class="tr"><div class="c" style="width:105px">LTC/BTC</div><div class="c up">0.0123</div></div>
  </div>

  <!-- balance -->
  <div class="grid-table" style="left:277px;top:131px;width:211px">
    <div class="th"><div class="c">YOUR BALANCE</div></div>
    <div class="tr"><div class="c" style="width:105px">BTC</div><div class="c">0.92176</div></div>
    <div class="tr"><div class="c" style="width:105px">LTC</div><div class="c">0</div></div>
    <div class="tr"><div class="c" style="width:105px">USD</div><div class="c">1987.45</div></div>
  </div>

  <!-- order entry -->
  <div class="order-tabs abs"><div class="tab-market">MARKET</div><div class="tab-limit">LIMIT</div></div>
  <div class="quote abs">
    <div class="quote-row">
      <div>Limit SELL<div class="quote-price">157<b>5.6</b>0</div></div>
      <div>Limit BUY<div class="quote-price">157<b>5.7</b>1</div></div>
    </div>
    <div class="qty-row"><div>Qty&nbsp; 20.0</div><div>Qty&nbsp; 20.0</div></div>
  </div>
  <svg class="abs" style="left:594px;top:164px" width="8" height="30" viewBox="0 0 8 30"><path d="M4 28V3M1 6l3-4 3 4" stroke="#bbb" fill="none"/></svg>
  <div class="input-label abs" style="left:512px;top:250px">Quantity</div>
  <div class="input-label abs" style="left:621px;top:250px">Limit</div>
  <div class="mini-field abs" style="left:512px;top:266px">50</div>
  <div class="mini-field abs" style="left:621px;top:266px">1576.63</div>

  <!-- order book -->
  <div class="grid-table book" style="left:512px;top:310px;width:210px">
    <div class="th"><div class="c" style="width:105px">PRICE</div><div class="c" style="border:0">VOLUME</div></div>
    <div class="tr bid"><div class="c">123</div><div class="c">0.233</div></div>
    <div class="tr bid"><div class="c">122</div><div class="c">0.334</div></div>
    <div class="tr bid"><div class="c">119</div><div class="c">2.321</div></div>
    <div class="tr bid"><div class="c">118</div><div class="c">0.343</div></div>
    <div class="tr bid"><div class="c">117</div><div class="c">0.22</div></div>
    <div class="tr bid"><div class="c">116</div><div class="c">0.025</div></div>
    <div class="tr bid"><div class="c">115</div><div class="c">0.5246</div></div>
    <div class="tr bid"><div class="c">114</div><div class="c">0.546</div></div>
    <div class="tr ask"><div class="c">113</div><div class="c">1.275</div></div>
    <div class="tr ask"><div class="c">112</div><div class="c">2.343</div></div>
    <div class="tr ask"><div class="c">111</div><div class="c">0.232</div></div>
    <div class="tr ask"><div class="c">110</div><div class="c">0.244</div></div>
    <div class="tr ask"><div class="c">109</div><div class="c">0.821</div></div>
    <div class="tr ask"><div class="c">108</div><div class="c">0.523</div></div>
    <div class="tr ask"><div class="c">109</div><div class="c">0.821</div></div>
    <div class="tr ask"><div class="c">108</div><div class="c">0.523</div></div>
  </div>

  <!-- chart -->
  <div class="chart-toolbar abs">
    <div class="tool" style="left:15px;width:149px"><span class="period">1D</span><span class="caret"></span></div>
    <div class="tool" style="left:172px;width:94px">Chart<span class="caret"></span></div>
    <div class="tool" style="left:275px;width:93px">Studies<span class="caret"></span></div>
    <svg class="abs" style="left:376px;top:20px" width="22" height="14" viewBox="0 0 22 14"><circle cx="7" cy="7" r="4.5" fill="none" stroke="#fff" stroke-width="3" stroke-dasharray="2.2 1.3"/><circle cx="7" cy="7" r="2" fill="#fff"/><path d="M15 6h5l-2.5 3z" fill="#fff"/></svg>
    <div class="tool" style="left:409px;width:20px;padding:5px 6px;font-weight:700;color:var(--blue)">F</div>
  </div>
  <div class="chart-area abs">
    <svg width="445" height="320" viewBox="43 320 445 320" role="img" aria-label="Candlestick price chart, August to December">
      <rect x="59" y="335" width="93" height="24" rx="2" fill="#fff"/>
      <rect x="130" y="335" width="22" height="24" fill="#555"/>
      <path d="M138 346h6l-3 3z" fill="#ddd"/>
      <text x="66" y="351" font-size="11" fill="#555" font-family="Cabin,sans-serif">Chart</text>
      <g font-family="Cabin,sans-serif" font-size="11" fill="#ddd">
        <text x="264" y="344">O: 141.93</text><text x="343" y="344">H: 142.10</text><text x="419" y="344">V: 119.09m</text>
        <text x="264" y="362">C: 141.02</text><text x="343" y="362">L: 140.80</text>
      </g>
      <g stroke="#2a2a2a" stroke-width="1">
        <path d="M58 394H438M58 410H438M58 427H438M58 443H438M58 459H438M58 476H438M58 492H438M58 509H438M58 525H438M58 541H438M58 558H438M58 574H438M58 591H438M58 607H438"/>
        <path d="M89 380V612M168 380V612M232 380V612M304 380V612M375 380V612"/>
      </g>
      <path d="M58 612H438M438 380V612" stroke="#666"/>
      <g font-family="Cabin,sans-serif" font-size="8" fill="#ddd">
        <text x="442" y="397">148.00</text><text x="442" y="413">147.00</text><text x="442" y="430">146.00</text><text x="442" y="446">145.00</text>
        <text x="442" y="462">144.00</text><text x="442" y="479">143.00</text><text x="442" y="512">141.00</text><text x="442" y="528">140.00</text>
        <text x="442" y="544">139.00</text><text x="442" y="561">138.00</text><text x="442" y="577">137.00</text><text x="442" y="594">136.00</text><text x="442" y="610">135.00</text>
      </g>
      <rect x="439" y="485" width="30" height="12" fill="#6ab04c"/>
      <text x="441" y="494" font-family="Cabin,sans-serif" font-size="8" fill="#fff">142.14</text>
      <path stroke="#bbb" stroke-width="1" d="M73.5 576V605M81.5 568V605M89.5 535V580M97.5 535V564M105.5 519V564M113.5 502V531M121.5 502V523M129.5 486V523M137.5 486V506M145.5 478V506M153.5 478V501M161.5 478V501M169.5 470V490M177.5 445V482M185.5 437V457M193.5 404V449M201.5 396V416M209.5 396V424M217.5 412V449M225.5 437V465M233.5 429V465M241.5 412V441M249.5 412V449M257.5 437V474M265.5 445V474M273.5 445V482M281.5 470V514M289.5 502V523M297.5 494V523M305.5 486V506M313.5 486V531M321.5 519V556M329.5 544V580M337.5 568V597M345.5 585V613M353.5 552V605M361.5 519V564M369.5 494V531"/>
      <g fill="var(--green)">
        <rect x="79" y="574" width="5" height="25"/><rect x="87" y="541" width="5" height="33"/><rect x="103" y="525" width="5" height="33"/>
        <rect x="111" y="508" width="5" height="17"/><rect x="127" y="492" width="5" height="25"/><rect x="143" y="484" width="5" height="16"/>
        <rect x="159" y="484" width="5" height="11"/><rect x="167" y="476" width="5" height="8"/><rect x="175" y="451" width="5" height="25"/>
        <rect x="183" y="443" width="5" height="8"/><rect x="191" y="410" width="5" height="33"/><rect x="199" y="402" width="5" height="8"/>
        <rect x="231" y="435" width="5" height="24"/><rect x="239" y="418" width="5" height="17"/><rect x="263" y="451" width="5" height="17"/>
        <rect x="295" y="500" width="5" height="17"/><rect x="303" y="492" width="5" height="8"/><rect x="351" y="558" width="5" height="41"/>
        <rect x="359" y="525" width="5" height="33"/><rect x="367" y="500" width="5" height="25"/>
      </g>
      <g fill="var(--red)">
        <rect x="71" y="582" width="5" height="17"/><rect x="95" y="541" width="5" height="17"/><rect x="119" y="508" width="5" height="9"/>
        <rect x="135" y="492" width="5" height="8"/><rect x="151" y="484" width="5" height="11"/><rect x="207" y="402" width="5" height="16"/>
        <rect x="215" y="418" width="5" height="25"/><rect x="223" y="443" width="5" height="16"/><rect x="247" y="418" width="5" height="25"/>
        <rect x="255" y="443" width="5" height="25"/><rect x="271" y="451" width="5" height="25"/><rect x="279" y="476" width="5" height="32"/>
        <rect x="287" y="508" width="5" height="9"/><rect x="311" y="492" width="5" height="33"/><rect x="319" y="525" width="5" height="25"/>
        <rect x="327" y="550" width="5" height="24"/><rect x="335" y="574" width="5" height="17"/><rect x="343" y="591" width="5" height="8"/>
      </g>
      <g>
        <circle cx="168" cy="592" r="6" fill="#ddd"/><path d="M165 592h6" stroke="#000" stroke-width="1.5"/>
        <path d="M176 592l40-2" stroke="#444" stroke-width="3" stroke-linecap="round"/>
        <circle cx="232" cy="592" r="6" fill="#ddd"/><path d="M229 592h6M232 589v6" stroke="#000" stroke-width="1.5"/>
      </g>
      <g font-family="Cabin,sans-serif" font-size="10" fill="#ddd" text-anchor="middle">
        <text x="89" y="624">aug</text><text x="168" y="624">sep</text><text x="232" y="624">oct</text><text x="304" y="624">nov</text><text x="375" y="624">dec</text>
      </g>
    </svg>
  </div>

  <!-- history -->
  <div class="hist-tabs abs"><div class="active">ORDERS</div><div>HISTORY</div><div>TRANSACTIONS</div></div>
  <div class="grid-table" style="left:43px;top:689px;width:445px">
    <div class="th" style="background:#333;height:29px">
      <div class="c" style="width:87px">TICKER</div>
      <div class="c" style="width:185px">TIME<svg class="sort" width="6" height="4" viewBox="0 0 6 4"><path d="M0 4L3 0 6 4z" fill="#bbb"/></svg></div>
      <div class="c" style="width:86px">PRICE<svg class="sort" width="6" height="9" viewBox="0 0 6 9"><path d="M0 3.5L3 0 6 3.5zM0 5.5L3 9 6 5.5z" fill="#bbb"/></svg></div>
      <div class="c">VOLUME</div>
    </div>
    <div class="tr"><div class="c" style="width:87px">BTC/USD</div><div class="c" style="width:185px">12:23&nbsp; 12.10.2014</div><div class="c" style="width:86px">634.34</div><div class="c">0.23</div></div>
    <div class="tr"><div class="c" style="width:87px">LTC/USD</div><div class="c" style="width:185px">11:23&nbsp; 12.10.2014</div><div class="c" style="width:86px">23.45</div><div class="c">0.01</div></div>
  </div>

  <!-- sidebar -->
  <aside class="abs" style="left:745px;top:128px;width:212px">
    <h2 class="side-title">LATEST NEWS</h2>
    <article class="news-item"><h3>Lorem ipsum dolor sit amet for amt...</h3><div class="news-date">25 March 2014</div><p>Lorem ipsum dolor sit amet, consec adipiscing elit, sed diam nonummyutpat...</p></article>
    <article class="news-item"><h3>Lorem ipsum dolor sit amet for amt...</h3><div class="news-date">25 March 2014</div><p>Lorem ipsum dolor sit amet, consec adipiscing elit, sed diam nonummyutpat...</p></article>
    <article class="news-item"><h3>Lorem ipsum dolor sit amet for amt...</h3><div class="news-date">25 March 2014</div><p>Lorem ipsum dolor sit amet, consec adipiscing elit, sed diam nonummyutpat...</p></article>
    <article class="news-item" style="border:0"><h3>Lorem ipsum dolor sit amet for amt...</h3><div class="news-date">25 March 2014</div><p>Lorem ipsum dolor sit amet, consec adipiscing elit, sed diam nonummyutpat...</p></article>
    <h2 class="side-title" style="margin-top:22px">SOCIAL FEEDS</h2>
    <div class="post">Proin gravida nibh vel velit auctor aliquet.<br><a>http://vtr.co/Splgmgyv76</a><div class="post-age">About 28 days ago</div></div>
    <div class="post">Proin gravida nibh vel velit auctor aliquet.<br><a>http://vtr.co/Splgmgyv76</a><div class="post-age">About 28 days ago</div></div>
    <div class="post" style="border:0">Proin gravida nibh vel velit auctor aliquet.<br><a>http://vtr.co/Splgmgyv76</a><div class="post-age">About 28 days ago</div></div>
  </aside>

  <footer class="site-footer abs">
    <div class="copy">© 2014 VelmoraTrade. All Rights Reserved.</div>
    <div class="links">About Us <span>|</span> Terms and Conditions <span>|</span> FAQ</div>
  </footer>

</div>
</body>
</html>
```